Exciting & Elegant Stationary Pack

Stationary consists of
1. Letter head / Envelope
2. Business Card
3. Invoice
4. 40x40mm sticker

Attached files;

1. Logo (Other formats available on request)
2. MS word Doc - For information and description of design
3. Website image (This will be our new website so use the colours so everything ties together)
4. Sample of stationary pack we like, but feel free to be creative

Target Market(s)

Home improvement

Industry/Entity Type

Construction

Font styles to use
Other font styles liked:
• Leave up to designer - We like font used on (website attached image)

Requirements
Must have
• Please look at uploaded file of sample website and use colours
Nice to have
• Any type of business card design - eg. metal, die cut, embossed, etc...

```html
<!DOCTYPE html>
<html lang="en">
<head>
<meta charset="utf-8">
<title>Setline Tiling — Stationery Pack</title>
<link href="https://fonts.googleapis.com/css2?family=Montserrat:wght@400;600;700;800&family=Roboto:wght@400;500&family=Dancing+Script:wght@600&display=swap" rel="stylesheet">
<style>
  :root {
    --navy: #10446a;
    --red: #d0272e;
    --white: #ffffff;
    --paper-bg: #e4e4e6;
    --ink: #1f2a33;
    --rule: #8a8f94;
  }
  * { box-sizing: border-box; margin: 0; padding: 0; }
  html, body { width: 1189px; height: 1200px; overflow: hidden; background: var(--paper-bg); }
  .board { position: relative; width: 1457px; height: 1468px; transform: scale(0.8161); transform-origin: 0 0; font-family: "Roboto", Arial, sans-serif; color: var(--ink); }
  .item { position: absolute; background: var(--white); overflow: hidden; }
  .band { position: absolute; left: 0; right: 0; }
  .navy { background: var(--navy); }
  .red { background: var(--red); }

  .brand { position: absolute; display: flex; align-items: center; gap: 8px; font-family: "Montserrat", sans-serif; font-weight: 800; color: var(--navy); letter-spacing: 0.02em; white-space: nowrap; }
  .brand .mark { display: inline-block; background: var(--navy); flex: none; }
  .brand.on-dark { color: var(--white); }
  .brand.on-dark .mark { background: var(--white); }
  .brand.centered { left: 0; right: 0; justify-content: center; }

  .contact { position: absolute; text-align: right; font-family: "Montserrat", sans-serif; color: var(--navy); font-size: 9px; line-height: 10px; }
  .contact .label { color: var(--red); }
  .contact .ico { display: inline-block; width: 7px; height: 7px; background: var(--red); margin-left: 3px; vertical-align: -1px; }

  /* folder */
  .folder { left: 53px; top: 54px; width: 514px; height: 664px; }
  .folder .url { position: absolute; bottom: 36px; width: 100%; text-align: center; color: var(--white); font-family: "Montserrat", sans-serif; font-size: 9px; }

  /* letterhead */
  .letter { left: 601px; top: 59px; width: 513px; height: 662px; }
  .letter .co-name { position: absolute; right: 41px; top: 28px; font-family: "Montserrat", sans-serif; font-weight: 600; font-size: 12px; color: var(--navy); }
  .letter .recipient { position: absolute; left: 40px; top: 187px; font-size: 9px; line-height: 10px; }
  .letter .recipient strong { display: block; font-size: 11px; font-weight: 500; margin-bottom: 6px; }
  .letter .body { position: absolute; left: 40px; top: 261px; width: 436px; font-size: 9px; line-height: 15px; }
  .letter .body p + p { margin-top: 15px; }
  .letter .signoff { position: absolute; left: 40px; top: 500px; font-size: 9px; }
  .letter .signature { position: absolute; left: 40px; top: 517px; font-family: "Dancing Script", cursive; font-size: 30px; color: var(--ink); }
  .letter .signer { position: absolute; left: 40px; top: 564px; font-size: 10px; line-height: 12px; }
  .letter .signer strong { font-weight: 500; }

  /* erasers */
  .eraser { position: absolute; height: 62px; box-shadow: 0 3px 6px rgba(0,0,0,.15); }
  .eraser-white { left: 1207px; top: 118px; width: 158px; background: var(--white); }
  .eraser-white .cap { position: absolute; right: 0; top: 0; bottom: 0; width: 28px; background: #2b2b2b; }
  .eraser-navy { left: 1200px; top: 253px; width: 160px; height: 65px; background: var(--navy); }
  .eraser-navy .cap { position: absolute; right: 0; top: 0; bottom: 0; width: 28px; background: #f2f2f2; }

  /* notebook */
  .notebook { left: 1154px; top: 381px; width: 246px; height: 340px; }
  .notebook .url { position: absolute; bottom: 17px; width: 100%; text-align: center; color: var(--white); font-size: 4px; }

  /* envelopes */
  .envelope-dl { left: 50px; top: 856px; width: 446px; height: 222px; }
  .envelope-dl .addr { position: absolute; top: 199px; width: 100%; text-align: center; color: var(--white); font-family: "Montserrat", sans-serif; font-size: 7px; }
  .envelope-back { left: 51px; top: 1189px; width: 446px; height: 223px; }
  .envelope-back .flap { position: absolute; left: 0; right: 0; top: 0; }
  .envelope-back .url { position: absolute; top: 196px; width: 100%; text-align: center; font-family: "Montserrat", sans-serif; font-weight: 700; font-size: 6px; color: var(--ink); }

  /* sticker */
  .sticker { position: absolute; left: 605px; top: 770px; width: 172px; height: 172px; border-radius: 50%; background: var(--navy); overflow: hidden; }
  .sticker .ring { position: absolute; inset: 5px; border: 1.5px solid var(--white); border-radius: 50%; }
  .sticker .brand { top: 56px; font-size: 11.5px; gap: 6px; }
  .sticker .phone { position: absolute; top: 92px; width: 100%; text-align: center; font-family: "Montserrat", sans-serif; font-weight: 800; font-size: 15px; color: var(--white); }
  .sticker .addr { position: absolute; top: 121px; width: 100%; text-align: center; font-family: "Montserrat", sans-serif; font-size: 8px; line-height: 10px; color: var(--white); }

  /* business cards */
  .card-front { left: 528px; top: 986px; width: 327px; height: 186px; background: var(--navy); }
  .card-front .brand { top: 68px; font-size: 24px; gap: 10px; }
  .card-front .url { position: absolute; bottom: 0; left: 0; right: 0; height: 19px; background: var(--red); color: var(--white); text-align: center; font-family: "Montserrat", sans-serif; font-size: 9px; line-height: 19px; }
  .card-back { left: 527px; top: 1222px; width: 330px; height: 188px; }
  .card-back .title { position: absolute; left: 15px; top: 22px; font-family: "Montserrat", sans-serif; font-weight: 800; font-size: 14px; color: var(--navy); }
  .card-back .person { position: absolute; left: 15px; top: 66px; font-family: "Montserrat", sans-serif; }
  .card-back .person strong { display: block; font-size: 12px; font-weight: 700; color: var(--navy); }
  .card-back .person span { font-size: 9px; color: var(--red); }
  .card-back .details { position: absolute; left: 15px; top: 104px; list-style: none; font-family: "Montserrat", sans-serif; font-size: 8.5px; line-height: 11.5px; color: var(--navy); }
  .card-back .details i { display: inline-block; width: 8px; height: 8px; background: var(--red); margin-right: 6px; vertical-align: -1px; }
  .card-back .licence { position: absolute; left: 15px; top: 145px; font-family: "Montserrat", sans-serif; font-size: 8.5px; color: var(--red); }
  .card-back .foot { position: absolute; left: 0; right: 0; top: 162px; height: 17px; background: var(--navy); color: var(--white); font-family: "Montserrat", sans-serif; font-size: 8.5px; line-height: 17px; padding-left: 15px; }
  .card-back .foot-red { position: absolute; left: 0; right: 0; top: 179px; bottom: 0; background: var(--red); }

  /* invoice */
  .invoice { left: 887px; top: 749px; width: 513px; height: 663px; font-family: "Montserrat", sans-serif; }
  .invoice .co-name { position: absolute; right: 42px; top: 29px; font-weight: 700; font-size: 15px; color: var(--navy); }
  .invoice .meta { position: absolute; font-size: 9.5px; color: var(--navy); }
  .invoice .meta b { color: var(--red); font-weight: 700; }
  .invoice table { position: absolute; left: 43px; top: 206px; width: 428px; border-collapse: collapse; font-family: "Roboto", Arial, sans-serif; font-size: 6.5px; }
  .invoice th { font-weight: 700; border: 1px solid var(--rule); height: 10px; line-height: 8px; }
  .invoice td { border-left: 1px solid var(--rule); border-right: 1px solid var(--rule); border-bottom: 1px solid #b9bcbf; height: 10.4px; line-height: 8px; padding: 0 5px; }
  .invoice td.num { text-align: right; }
  .invoice .totals { position: absolute; left: 246px; top: 520px; width: 225px; border-collapse: collapse; font-family: "Roboto", Arial, sans-serif; font-size: 7px; font-weight: 700; }
  .invoice .totals td { border: 1px solid var(--rule); height: 21px; padding: 0 4px; vertical-align: bottom; }
  .invoice .totals tr:last-child td { height: 24px; font-size: 8.5px; }
</style>
</head>
<body>
<main class="board">

  <!-- presentation folder -->
  <section class="item folder" aria-label="Presentation folder">
    <div class="brand" style="left:150px;top:80px;font-size:30px;"><span class="mark" style="width:20px;height:20px"></span>SETLINE TILING</div>
    <div class="band navy" style="top:234px;height:350px"></div>
    <div class="band red" style="top:584px;height:80px"></div>
    <p class="url">www.setlinetiling.com.au</p>
  </section>

  <!-- letterhead -->
  <section class="item letter" aria-label="Letterhead">
    <div class="brand" style="left:18px;top:32px;font-size:17px;"><span class="mark" style="width:12px;height:12px"></span>SETLINE TILING</div>
    <p class="co-name">SETLINE TILING</p>
    <div class="contact" style="right:41px;top:51px;">
      <div><span class="label">[ABN]:</span> 12 345 678 901</div>
      <div>0400 555 132<span class="ico"></span></div>
      <div>WWW.SETLINETILING.COM.AU<span class="ico"></span></div>
      <div>PO BOX 48 FAIRVIEW PARK NSW 2170<span class="ico"></span></div>
    </div>
    <div class="recipient"><strong>ALEX REED</strong>Street Name,City Name.<br>Zip Coad 0000</div>
    <div class="body">
      <p>Lorem Ipsum is simply dummy text of the printing and typesetting industry. Lorem Ipsum has been the industry's standard dummy text ever since the 1500s, when an unknown printer took a galley of type and scrambled it to make a type specimen book. It has survived not only five centuries, but also the leap into electronic typesetting, remaining essentially unchanged. It was popularised in the 1960s with the release of Letraset sheets containing Lorem Ipsum passages, and more recently with desktop publishing software like Aldus PageMaker including versions of Lorem Ipsum.</p>
      <p>It is a long established fact that a reader will be distracted by the readable content of a page when looking at its layout. The point of using Lorem Ipsum is that it has a more-or-less normal distribution of letters, as opposed to using 'Content here, content here', making it look like readable English. Many desktop publishing packages and web page editors now use Lorem Ipsum as their default model text, and a search for 'lorem ipsum' will uncover many web sites still in their infancy. Various versions have evolved over the years, sometimes by accident, sometimes on purpose (injected humour and the like).</p>
    </div>
    <p class="signoff">Regards,</p>
    <p class="signature">Sam Porter</p>
    <p class="signer"><strong>Sam Porter</strong><br>General Maneger</p>
    <div class="band navy" style="top:616px;height:31px"></div>
    <div class="band red" style="top:647px;height:15px"></div>
  </section>

  <!-- erasers -->
  <div class="eraser eraser-white" aria-label="Branded eraser">
    <div class="brand" style="left:34px;top:24px;font-size:9px;"><span class="mark" style="width:7px;height:7px"></span>SETLINE TILING</div>
    <span class="cap"></span>
  </div>
  <div class="eraser eraser-navy" aria-label="Branded eraser">
    <div class="brand on-dark" style="left:14px;top:25px;font-size:10px;"><span class="mark" style="width:7px;height:7px"></span>SETLINE TILING</div>
    <span class="cap"></span>
  </div>

  <!-- notebook -->
  <section class="item notebook" aria-label="Notebook cover">
    <div class="brand" style="left:60px;top:36px;font-size:13px;"><span class="mark" style="width:9px;height:9px"></span>SETLINE TILING</div>
    <div class="band navy" style="top:119px;height:180px"></div>
    <div class="band red" style="top:299px;height:41px"></div>
    <p class="url">www.setlinetiling.com.au</p>
  </section>

  <!-- DL envelope front -->
  <section class="item envelope-dl" aria-label="Envelope front">
    <div class="brand" style="left:14px;top:24px;font-size:13px;"><span class="mark" style="width:9px;height:9px"></span>SETLINE TILING</div>
    <div class="band navy" style="top:195px;height:19px"></div>
    <div class="band red" style="top:214px;height:8px"></div>
    <p class="addr">PO BOX 48 FAIRVIEW PARK NSW 2170</p>
  </section>

  <!-- envelope back -->
  <section class="item envelope-back" aria-label="Envelope back">
    <svg class="flap" width="446" height="64" viewBox="0 0 446 64" aria-hidden="true">
      <path d="M0 0 H446 L438 56 Q437 62 431 62 H14 Q8 62 7 56 Z" fill="var(--navy)"/>
    </svg>
    <div class="brand on-dark centered" style="top:20px;font-size:12px;"><span class="mark" style="width:8px;height:8px"></span>SETLINE TILING</div>
    <p class="url">www.setlinetiling.com.au</p>
  </section>

  <!-- 40x40 sticker -->
  <section class="sticker" aria-label="Round sticker">
    <span class="ring"></span>
    <div class="brand on-dark centered"><span class="mark" style="width:8px;height:8px"></span>SETLINE TILING</div>
    <p class="phone">0400 555 132</p>
    <p class="addr">PO Box 48 Fairview Park<br>NSW 2170</p>
  </section>

  <!-- business card front -->
  <section class="item card-front" aria-label="Business card front">
    <div class="brand on-dark centered"><span class="mark" style="width:15px;height:15px"></span>SETLINE TILING</div>
    <p class="url">www.setlinetiling.com.au</p>
  </section>

  <!-- business card back -->
  <section class="item card-back" aria-label="Business card back">
    <p class="title">SETLINE TILING</p>
    <div class="person"><strong>Linh Tran</strong><span>Project Manager</span></div>
    <ul class="details">
      <li><i></i>0400 555 132</li>
      <li><i></i>info@setlinetiling.com.au</li>
      <li><i></i>www.setlinetiling.com.au</li>
    </ul>
    <p class="licence">LICENSE: 204519c</p>
    <p class="foot">PO BOX 48 FAIRVIEW PARK NSW 2170</p>
    <span class="foot-red"></span>
  </section>

  <!-- tax invoice -->
  <section class="item invoice" aria-label="Tax invoice">
    <div class="brand" style="left:57px;top:34px;font-size:20px;"><span class="mark" style="width:13px;height:13px"></span>SETLINE TILING</div>
    <p class="co-name">SETLINE TILING</p>
    <div class="contact" style="right:42px;top:59px;font-size:9.5px;line-height:12px;">
      <div><span class="label">[ABN]:</span> 12 345 678 901</div>
      <div>0400 555 132<span class="ico"></span></div>
      <div>WWW.SETLINETILING.COM.AU<span class="ico"></span></div>
      <div>PO BOX 48 FAIRVIEW PARK NSW 2170<span class="ico"></span></div>
    </div>
    <p class="meta" style="left:43px;top:140px;"><b>TAX INVOICE:</b></p>
    <p class="meta" style="right:42px;top:137px;font-size:11px;"><b>DATE:</b> 31/08/2016</p>
    <p class="meta" style="left:43px;top:176px;"><b>TO:</b> NORTHGATE BUILDERS</p>
    <p class="meta" style="right:40px;top:176px;"><b>SITE ADDRESS:</b> HARLOW RD EASTWOOD</p>
    <table>
      <colgroup><col style="width:203px"><col style="width:60px"><col style="width:56px"><col style="width:109px"></colgroup>
      <thead><tr><th>DESCRIPTION</th><th>RATE</th><th>UNIT</th><th>TOTAL</th></tr></thead>
      <tbody>
        <tr><td>Service</td><td class="num">$1</td><td class="num">1</td><td class="num">$1.00</td></tr>
        <tr><td></td><td></td><td></td><td class="num">$0.00</td></tr>
        <tr><td></td><td></td><td></td><td class="num">$0.00</td></tr>
        <tr><td></td><td></td><td></td><td class="num">$0.00</td></tr>
        <tr><td></td><td></td><td></td><td class="num">$0.00</td></tr>
        <tr><td></td><td></td><td></td><td class="num">$0.00</td></tr>
        <tr><td></td><td></td><td></td><td class="num">$0.00</td></tr>
        <tr><td></td><td></td><td></td><td class="num">$0.00</td></tr>
        <tr><td></td><td></td><td></td><td></td></tr><tr><td></td><td></td><td></td><td></td></tr>
        <tr><td></td><td></td><td></td><td></td></tr><tr><td></td><td></td><td></td><td></td></tr>
        <tr><td></td><td></td><td></td><td></td></tr><tr><td></td><td></td><td></td><td></td></tr>
        <tr><td></td><td></td><td></td><td></td></tr><tr><td></td><td></td><td></td><td></td></tr>
        <tr><td></td><td></td><td></td><td></td></tr><tr><td></td><td></td><td></td><td></td></tr>
        <tr><td></td><td></td><td></td><td></td></tr><tr><td></td><td></td><td></td><td></td></tr>
        <tr><td></td><td></td><td></td><td></td></tr><tr><td></td><td></td><td></td><td></td></tr>
        <tr><td></td><td></td><td></td><td></td></tr><tr><td></td><td></td><td></td><td></td></tr>
        <tr><td></td><td></td><td></td><td></td></tr><tr><td></td><td></td><td></td><td></td></tr>
        <tr><td></td><td></td><td></td><td></td></tr><tr><td></td><td></td><td></td><td></td></tr>
        <tr><td></td><td></td><td></td><td></td></tr>
      </tbody>
    </table>
    <table class="totals">
      <colgroup><col style="width:116px"><col></colgroup>
      <tr><td>SUB-TOTAL</td><td>$<br>- &nbsp;1.00</td></tr>
      <tr><td>G.S.T 10%</td><td>$<br>- &nbsp;0.10</td></tr>
      <tr><td>TOTAL DUE</td><td>$<br>- &nbsp;1.10</td></tr>
    </table>
    <div class="band navy" style="top:627px;height:24px"></div>
    <div class="band red" style="top:651px;height:12px"></div>
  </section>

</main>
</body>
</html>
```